Livescore site

New livescore site (tallyhop.com) with all relevant live sports statistics is looking for a webdesign and logo. Features such as:
- live events (goals, cards, etc)
- fixtures
- tables
- stats.

We feature all kinds of different sports including of course Soccer, Tennis, Basketball, Boxing, Golf etc.
One of the unique features is a chat tool connected to all games to allow more interaction between user and content. To share comments a user will have to sign up, only with email adress or their friendnook login details. Also features such as man of the Match and The Best Goals will be available on tallyhop.com. Also we wil have a feature that allows you to share game start (i.e. Corvale-Dunmoor) with a comment attached ("guys, are you coming over for beers?") as well as sharing goal scorer, game result, also with comments attached. We want a social media feeling to the design and the combination of sports. (Must include logo as well combining the fealing of sports, chat, social media/web2.0)

examples of site we like (only for inspiration)

www.rapidmarks.com
http://www.fjelp.dk/livescore/

Hi designers,

we updated our design brief with an actual design on how we want the site presented. Colors, fonts etc. is up to you as long as you keep it simple. Logo we want with a speech bubble and representing Tallyhop.com and sports.

check the following link for further details.

http://www.tallyhop.com/TallyhopDOC.htm

```html
<!DOCTYPE html>
<html lang="en">
<head>
<meta charset="utf-8">
<title>Tallyhop.com – livescores and chating</title>
<link rel="stylesheet" href="https://fonts.googleapis.com/css2?family=Arimo:wght@400;700&display=swap">
<style>
:root{
  --page:#eeeeee;
  --white:#ffffff;
  --ink:#1d1d1d;
  --muted:#555555;
  --blue:#1a7fd0;
  --blue-dark:#0b5fa8;
  --blue-light:#3d9be3;
  --frame:#4a9ee0;
  --black:#111111;
  --line:#d4d4d4;
  --footer:#1b1b1b;
}
*{box-sizing:border-box;margin:0;padding:0}
html,body{width:884px;height:1200px;overflow:hidden}
body{background:var(--page);font-family:"Arimo",Arial,sans-serif;color:var(--ink);position:relative}
.abs{position:absolute}

/* top navigation */
.main-nav{left:283px;top:16px;display:flex;height:29px}
.main-nav a{display:block;width:84px;background:var(--black);color:var(--white);font-size:10px;font-weight:700;text-decoration:none;text-align:center;line-height:29px;border-right:1px solid #444}
.main-nav a.current{background:linear-gradient(var(--blue-light),var(--blue-dark));font-size:13px;width:83px;height:35px;line-height:35px}

/* header */
.brand{left:99px;top:50px;display:flex;align-items:center;gap:8px}
.brand-dot{width:72px;height:72px;border-radius:50%;background:var(--blue)}
.brand-name{font-size:29px;color:var(--blue);font-weight:400;line-height:1}
.brand-tag{font-size:14px;color:var(--ink);margin-top:4px;padding-top:3px;border-top:1px solid var(--ink);width:150px}
.user-links{left:558px;top:73px;font-size:10px;color:var(--ink)}
.user-links b{margin-right:10px}
.search{left:579px;top:99px;display:flex;gap:9px}
.search input{width:152px;height:18px;border:1px solid #ccc;background:var(--white)}
.search button{width:46px;height:18px;background:var(--black);color:var(--white);border:0;font:700 10px "Arimo",Arial,sans-serif}

/* panels */
.panel{background:var(--white);border:1px solid var(--frame)}
.sport-tabs{display:flex;height:25px;background:linear-gradient(#e6e6e6,#bdbdbd);font-size:12px;color:#222}
.sport-tabs span{padding:0 13px;line-height:25px}
.sport-tabs span + span::before{content:"|";margin-left:-16px;margin-right:13px;color:#555}
.sport-tabs .on{background:linear-gradient(var(--blue-light),var(--blue-dark));color:var(--white);font-weight:700;padding:0 12px;margin-right:4px}
.sport-tabs .on + span::before{content:""}

/* results hero */
.results{left:99px;top:141px;width:496px;height:299px;border:1px solid var(--frame);overflow:hidden}
.results-bg{position:absolute;inset:25px 0 0 0;background:linear-gradient(160deg,#3aa0ea,#1778c8 60%,#2a8dda)}
.results-body{position:absolute;top:31px;left:20px;right:0;color:var(--white)}
.results-body h2{font-size:18px;font-weight:700}
.results-body h3{font-size:13px;font-weight:700;margin:2px 0 6px}
.result-row{display:flex;height:19.7px;align-items:center;font-size:10px;font-weight:700;white-space:nowrap}
.result-row .st{width:74px}
.result-row .home{width:140px}
.result-row .score{width:100px;text-align:center;font-size:13px}
.result-row .away{width:160px;padding-left:13px}

/* banner slots */
.banner{background:linear-gradient(#ffffff,#eaeaea);border:1px solid var(--frame);display:flex;align-items:center;justify-content:center;font-weight:700;font-size:18px}

/* latest scores */
.scores{left:99px;top:457px;width:496px;height:223px}
.scores h4{font-size:11px;margin:10px 0 6px 12px}
.scores h5{font-size:10px;margin:0 0 2px 12px}
.score-row{display:flex;height:13.9px;align-items:center;font-size:10px;color:#222;white-space:nowrap}
.score-row span{flex-shrink:0}
.score-row span:nth-child(1){width:97px;padding-left:32px}
.score-row span:nth-child(2){width:66px}
.score-row span:nth-child(3){width:49px}
.score-row span:nth-child(4){width:42px}
.score-row span:nth-child(5){width:92px}
.score-row span:nth-child(6){width:44px}

/* live match list */
.block-head{height:25px;background:linear-gradient(var(--blue-light),var(--blue-dark));color:var(--white);font-size:13px;font-weight:700;line-height:25px;padding-left:8px}
.matches{left:607px;top:457px;width:178px;height:223px}
.matches ul{list-style:none;font-size:10px;padding:8px 0 0 7px}
.matches li{height:16.8px;display:flex;align-items:center}
.matches li.country{font-weight:700}
.matches .mk{width:10px;height:9px;background:#222;margin-right:12px;color:#fff;font-size:7px;line-height:9px;text-align:center}
.matches li.game{padding-left:28px}
.matches li.game::before{content:"»";font-weight:700;margin-right:8px}

/* standings */
.standings{left:99px;top:693px;width:370px;height:218px}
.standings .rows{padding-top:11px}
.stand-row{display:flex;height:16.9px;align-items:center;font-size:10px}
.stand-row span:nth-child(1){width:68px;padding-left:18px}
.stand-row span:nth-child(2){width:92px}
.stand-row span:nth-child(3){width:83px}
.stand-row span:nth-child(4){width:58px}

/* chat */
.chat{left:481px;top:693px;width:304px;height:218px}
.chat-log{margin:5px 4px 0;height:124px;border:1px solid #bbb;position:relative;overflow:hidden}
.chat-log .scroll{position:absolute;right:0;top:0;bottom:0;width:9px;background:#eee;border-left:1px solid #bbb}
.msg{border-bottom:1px solid #ddd;font-size:7px;padding:2px 14px 3px 3px;position:relative;height:18px;display:flex;align-items:flex-end;gap:4px;white-space:nowrap}
.msg.tall{height:27px}
.msg.top{height:8px}
.msg .av{width:12px;height:12px;background:#9aa8b4}
.msg time{position:absolute;right:14px;top:2px;color:#888;font-size:6px}
.msg b{text-decoration:underline}
.chat-tools{font-size:7px;text-align:right;padding:3px 8px 2px;color:#333}
.chat-input{margin:0 4px;height:14px;border:1px solid #9c9;font-size:7px;color:#999;padding-left:4px;line-height:12px}
.chat-foot{display:flex;justify-content:space-between;font-size:7px;padding:3px 4px 0}
.chat-foot .btn{border:1px solid #777;padding:0 3px;background:#eee}
.chat-meta{font-size:7px;padding:3px 4px;display:flex;gap:10px}
.chat-meta .tag{border:1px solid #777;padding:0 2px}

/* ad slots */
.ad{top:928px;height:77px;background:var(--white);border:1px solid var(--frame);display:flex;align-items:center;justify-content:center;font-size:22px;font-weight:700;color:#222}

/* footer */
.site-footer{left:0;top:1047px;width:884px;height:126px;background:linear-gradient(#3a3a3a,var(--footer) 40%,#000)}
.feature{top:1067px;height:72px;width:216px;background:linear-gradient(var(--blue-light),var(--blue-dark));display:flex;overflow:hidden}
.feature h6{font-size:17px;line-height:20px;color:var(--white);font-weight:700;padding:14px 0 0 12px;width:122px;flex-shrink:0;white-space:nowrap}
.feature .art{flex:1;background:linear-gradient(135deg,#cfe3f3,#6fa6d6)}
.newsletter{left:569px;top:1067px;width:216px;height:72px;background:var(--blue)}
.newsletter .nl-head{background:var(--white);height:16px;font-size:10px;font-weight:700;color:var(--blue-dark);padding:2px 0 0 10px;position:relative}
.newsletter .nl-head::after{content:"";position:absolute;left:14px;bottom:-6px;border:6px solid transparent;border-top-color:var(--white);border-bottom:0}
.newsletter form{display:flex;gap:7px;padding:20px 0 0 12px}
.newsletter input{width:140px;height:17px;border:0;font-size:8px;padding-left:5px;color:#999}
.newsletter button{width:38px;height:15px;margin-top:1px;background:var(--black);color:var(--white);border:0;border-radius:7px;font:700 8px "Arimo",Arial,sans-serif}
.copyright{left:0;top:1173px;width:884px;height:27px;background:linear-gradient(var(--blue-light),var(--blue-dark));color:var(--white);font-size:8px;font-weight:700;text-align:center;line-height:27px}
</style>
</head>
<body>

<nav class="main-nav abs">
  <a class="current" href="#">Home</a>
  <a href="#">Live Scores</a>
  <a href="#">Statistics</a>
  <a href="#">Fixture</a>
  <a href="#">About Us</a>
  <a href="#">Contact Us</a>
</nav>

<header>
  <div class="brand abs">
    <div class="brand-dot"></div>
    <div>
      <div class="brand-name">Tallyhop.com</div>
      <div class="brand-tag">livescores and chating</div>
    </div>
  </div>
  <div class="user-links abs"><b>New User?</b> Register &nbsp;|&nbsp; Sign In &nbsp;|&nbsp; friendnook Login</div>
  <form class="search abs"><input type="text" aria-label="Search"><button type="button">Search</button></form>
</header>

<section class="results abs" aria-label="Latest series results">
  <div class="sport-tabs"><span class="on">Soccer</span><span>Hockey</span><span>Basketball</span><span>Tennis</span><span>Cricket</span><span>Handball</span></div>
  <div class="results-bg" role="img" aria-label="Blue-toned stadium pitch background"></div>
  <div class="results-body">
    <h2>Latest Series Results</h2>
    <h3>England - National Circuit</h3>
    <div class="result-row"><span class="st">FT</span><span class="home">Ashford Vale</span><span class="score">2 - 0</span><span class="away">Barrowick</span></div>
    <div class="result-row"><span class="st">FT</span><span class="home">Camden U.</span><span class="score">3 - 0</span><span class="away">Kettlebury</span></div>
    <div class="result-row"><span class="st">FT</span><span class="home">Dunmere</span><span class="score">2 - 2</span><span class="away">Lutley T.</span></div>
    <div class="result-row"><span class="st">FT</span><span class="home">Fleetmoor</span><span class="score">1 - 1</span><span class="away">Kidderfield</span></div>
    <div class="result-row"><span class="st">FT</span><span class="home">Forest Hollow</span><span class="score">3 - 4</span><span class="away">Eastmoor Borough</span></div>
    <div class="result-row"><span class="st">FT</span><span class="home">Gatefield</span><span class="score">0 - 0</span><span class="away">Grimsfield T.</span></div>
    <div class="result-row"><span class="st">FT</span><span class="home">Haybury</span><span class="score">1 - 2</span><span class="away">Newbury County</span></div>
    <div class="result-row"><span class="st">FT</span><span class="home">Mansmoor T.</span><span class="score">5 - 0</span><span class="away">Yorwick C.</span></div>
    <div class="result-row"><span class="st">FT</span><span class="home">Rushby &amp; Rovers</span><span class="score">2 - 0</span><span class="away">Hilston</span></div>
    <div class="result-row"><span class="st">FT</span><span class="home">Tamfield</span><span class="score">2 - 2</span><span class="away">Bathley City</span></div>
    <div class="result-row"><span class="st">FT</span><span class="home">Wrexbury</span><span class="score">2 - 1</span><span class="away">Southmere</span></div>
  </div>
</section>

<aside class="banner abs" style="left:607px;top:141px;width:178px;height:150px">Banner Add</aside>
<aside class="banner abs" style="left:607px;top:301px;width:178px;height:139px">Banner Add</aside>

<section class="scores panel abs" aria-label="Latest scores">
  <div class="sport-tabs"><span class="on">Soccer</span><span>Hockey</span><span>Basketball</span><span>Tennis</span><span>Cricket</span><span>Handball</span></div>
  <h4>Latest Scores / Results</h4>
  <h5>English Top League 2010:</h5>
  <div class="score-row"><span>13:45</span><span>Stokeley City</span><span>(2)</span><span>-</span><span>West Holm United</span><span>(0)</span><span>View Full Summary</span></div>
  <div class="score-row"><span>13:45</span><span>Stokeley City</span><span>(2)</span><span>-</span><span>West Holm United</span><span>(0)</span><span>View Full Summary</span></div>
  <div class="score-row"><span>13:45</span><span>Stokeley City</span><span>(2)</span><span>-</span><span>West Holm United</span><span>(0)</span><span>View Full Summary</span></div>
  <div class="score-row"><span>13:45</span><span>Stokeley City</span><span>(2)</span><span>-</span><span>West Holm United</span><span>(0)</span><span>View Full Summary</span></div>
  <div class="score-row"><span>13:45</span><span>Stokeley City</span><span>(2)</span><span>-</span><span>West Holm United</span><span>(0)</span><span>View Full Summary</span></div>
  <div class="score-row"><span>13:45</span><span>Stokeley City</span><span>(2)</span><span>-</span><span>West Holm United</span><span>(0)</span><span>View Full Summary</span></div>
  <div class="score-row"><span>13:45</span><span>Stokeley City</span><span>(2)</span><span>-</span><span>West Holm United</span><span>(0)</span><span>View Full Summary</span></div>
  <div class="score-row"><span>13:45</span><span>Stokeley City</span><span>(2)</span><span>-</span><span>West Holm United</span><span>(0)</span><span>View Full Summary</span></div>
  <div class="score-row"><span>13:45</span><span>Stokeley City</span><span>(2)</span><span>-</span><span>West Holm United</span><span>(0)</span><span>View Full Summary</span></div>
  <div class="score-row"><span>13:45</span><span>Stokeley City</span><span>(2)</span><span>-</span><span>West Holm United</span><span>(0)</span><span>View Full Summary</span></div>
</section>

<section class="matches panel abs" aria-label="Live match list">
  <div class="block-head">Live Match List:</div>
  <ul>
    <li class="country"><span class="mk">–</span>Argentina</li>
    <li class="game">Soccer Game 1</li>
    <li class="game">Soccer Game 2</li>
    <li class="game">Soccer Game 3</li>
    <li class="game">Soccer Game 4</li>
    <li class="country"><span class="mk">»</span>Brazil</li>
    <li class="country"><span class="mk">»</span>Chile</li>
    <li class="country"><span class="mk">»</span>Ecuador</li>
    <li class="country"><span class="mk">»</span>Japan</li>
    <li class="country"><span class="mk">»</span>Mexico</li>
    <li class="country"><span class="mk">»</span>Paraguay</li>
  </ul>
</section>

<section class="standings panel abs" aria-label="Standings table">
  <div class="block-head">Standings Table:</div>
  <div class="rows">
    <div class="stand-row"><span>01</span><span>Barcella</span><span>365 Points</span><span>30 GF</span><span>45 GS</span></div>
    <div class="stand-row"><span>02</span><span>Barcella</span><span>365 Points</span><span>30 GF</span><span>45 GS</span></div>
    <div class="stand-row"><span>03</span><span>Barcella</span><span>365 Points</span><span>30 GF</span><span>45 GS</span></div>
    <div class="stand-row"><span>04</span><span>Barcella</span><span>365 Points</span><span>30 GF</span><span>45 GS</span></div>
    <div class="stand-row"><span>05</span><span>Barcella</span><span>365 Points</span><span>30 GF</span><span>45 GS</span></div>
    <div class="stand-row"><span>06</span><span>Barcella</span><span>365 Points</span><span>30 GF</span><span>45 GS</span></div>
    <div class="stand-row"><span>07</span><span>Barcella</span><span>365 Points</span><span>30 GF</span><span>45 GS</span></div>
    <div class="stand-row"><span>08</span><span>Barcella</span><span>365 Points</span><span>30 GF</span><span>45 GS</span></div>
    <div class="stand-row"><span>09</span><span>Barcella</span><span>365 Points</span><span>30 GF</span><span>45 GS</span></div>
    <div class="stand-row"><span>10</span><span>Barcella</span><span>365 Points</span><span>30 GF</span><span>45 GS</span></div>
  </div>
</section>

<section class="chat panel abs" aria-label="Live chat">
  <div class="block-head">Live Chat:</div>
  <div class="chat-log">
    <div class="scroll"></div>
    <div class="msg top"></div>
    <div class="msg tall"><span class="av"></span><b>Rafiq52:</b> hi<time>Tue Sep 14, 10:20:40pm</time></div>
    <div class="msg tall"><span class="av"></span><b>Streamfan:</b> Hi<time>Wed Sep 15, 3:44:50pm</time></div>
    <div class="msg">KOBI: hi<time>Thu Sep 16, 9:07:35pm</time></div>
    <div class="msg">Orin4412: hi<time>Thu Sep 16, 2:32:45pm</time></div>
    <div class="msg">skipper: which is the best sever<time>Sun Sep 19, 4:05:22pm</time></div>
  </div>
  <div class="chat-tools">×&nbsp; T- &nbsp;A- &nbsp;B &nbsp;I &nbsp;U</div>
  <div class="chat-input">Add a comment</div>
  <div class="chat-foot"><span><b>1 person here</b></span><span class="btn">Set Name</span></div>
  <div class="chat-meta"><span class="tag">chatnest</span><span>Get your own</span><span>Manage</span></div>
</section>

<aside class="ad abs" style="left:99px;width:338px">Your Add Goes Here</aside>
<aside class="ad abs" style="left:447px;width:338px">Your Add Goes Here</aside>

<footer>
  <div class="site-footer abs"></div>
  <div class="feature abs" style="left:99px">
    <h6>GOAL OF<br>THE WEEK</h6>
    <div class="art" role="img" aria-label="Football photo for goal of the week"></div>
  </div>
  <div class="feature abs" style="left:336px">
    <h6>PLAYER OF<br>THE MONTH</h6>
    <div class="art" role="img" aria-label="Photo of the player of the month"></div>
  </div>
  <div class="newsletter abs">
    <div class="nl-head">Newsletter Sign-up</div>
    <form><input type="email" placeholder="Enter your email address..." aria-label="Email address"><button type="button">Submit</button></form>
  </div>
  <div class="copyright abs">Copyright © 2010 Tallyhop.com | All Rights Reserved</div>
</footer>

</body>
</html>
```